Banner ad to sell prefabricated holiday homes in New Zealand

Harbor Nest Homes build prefabricated homes in a factory that are then transported by truck to their site. It's coming into summer here in New Zealand and many people will be thinking about the holidays and wishing they had a holiday home.

The design should communicate some of the following benefits of our homes:
- Full project management
- Great value for money
- Delivered complete with all interior & exterior fittings
- Quality construction in our controlled factory

The banner ad will be displayed on a popular weather website www.skyvanecast.co.nz
Size: 760px x 120px
Would like it to be animated if but the size must be below 60kb.

I'll upload some nice holiday destination photos for backgrounds & some pictures of our holiday home designs for you to use.
Our main company colors are bright blue (pantone 3005) and light grey/silver.

Updatefor brief:
I would like the animation to show different text so that it's not all squashed up on the one image.
For example have "Prefabricated Holiday Homes" on one image & then it fades/changes to next image with "Delivered complete with all interior & exterior fittings". Or something like that with nice background images or pictures of our houses.

```html
<!DOCTYPE html>
<html lang="en">
<head>
<meta charset="utf-8">
<title>Harbor Nest Homes – Holiday Homes Banner</title>
<link rel="stylesheet" href="https://fonts.googleapis.com/css2?family=Libre+Baskerville:wght@700&display=swap">
<style>
  :root {
    --brand-blue: #1566b2;
    --white: #ffffff;
    --ink: #1a1f2b;
    --page-bg: #ecebe8;
    --photo-tone: #6d7279;
  }
  html, body {
    margin: 0;
    width: 1200px;
    height: 900px;
    overflow: hidden;
    background: var(--page-bg);
  }
  .banner {
    position: absolute;
    left: 30px;
    top: 360px;
    width: 1140px;
    height: 180px;
    font-family: "Libre Baskerville", "Times New Roman", serif;
    font-weight: 700;
    color: var(--white);
  }
  .banner-shapes {
    position: absolute;
    inset: 0;
    width: 100%;
    height: 100%;
  }
  .headline {
    position: absolute;
    left: 0;
    top: 20px;
    width: 258px;
    margin: 0;
    text-align: center;
    font-size: 26px;
    line-height: 44px;
    font-weight: 700;
  }
  .benefit {
    position: absolute;
    left: 794px;
    top: 42px;
    margin: 0;
    font-size: 23px;
    line-height: 25px;
    font-weight: 700;
  }
  .brand {
    position: absolute;
    left: 771px;
    top: 131px;
    height: 46px;
    display: flex;
    align-items: center;
    gap: 47px;
  }
  .brand-mark {
    width: 34px;
    height: 34px;
    background: var(--brand-blue);
  }
  .brand-name {
    font-size: 24px;
    font-weight: 700;
    color: var(--ink);
  }
</style>
</head>
<body>
  <section class="banner">
    <svg class="banner-shapes" viewBox="0 0 760 120" preserveAspectRatio="none" aria-hidden="true">
      <rect class="banner-base" width="760" height="120" fill="var(--white)"/>
      <polygon class="panel-left" points="0,0 194,0 152,120 0,120" fill="var(--brand-blue)"/>
      <polygon class="panel-right" points="539,0 760,0 760,86 509,86" fill="var(--brand-blue)"/>
    </svg>
    <svg class="banner-shapes" viewBox="0 0 760 120" preserveAspectRatio="none" role="img" aria-label="Photo of a dark grey prefabricated holiday home with a timber deck, outdoor chairs and mountains behind">
      <polygon class="house-photo" points="198,0 535,0 493,120 156,120" fill="var(--photo-tone)"/>
    </svg>

    <h1 class="headline">Prefabricated<br>Holiday Homes In<br>New Zealand</h1>
    <p class="benefit">Delivered complete with all<br>interior &amp; exterior fittings</p>

    <div class="brand">
      <span class="brand-mark"></span>
      <span class="brand-name">Harbor Nest Homes</span>
    </div>
  </section>
</body>
</html>
```